New eyelid plastic surgery office needs a business card design-Eyelid Specialists of the Brenwick

I recently used DraftHarbor for my logo design and was very pleased with creativity and results. It was a difficult decision for me. Now I would like to create a business card based on this logo, which I will attach.

The text should be easily legible as some of my patients have difficulty seeing, but I would like a subtle, sophisticated artistry also evident to make the card memorable. Would like the card based on a similar color scheme as the logo but the inverse or other complementary colors may prove interesting

A good question was asked...my concern about my visually impaired patients was really my desire to avoid italicized or calligraphic type fonts that may be hard to read. Standard font size for a business card would be fine. Thanks!

Thank you so much for the great work so far. I wanted to give you my particular contact information to see if that would change the look of the cards. Martin Holloway, MD Address: 2871 Larkspur Lane, Suite 215 Wilmington, NC 39512 Phone: 555-382-1946 Fax: 555-382-1947 Website: www.brenwickliddesign.example Please delete the email slot from the card. Thanks so much!

Reason: Last minute consideration. So many great revisions right now!

Plastic

```html
<!DOCTYPE html>
<html lang="en">
<head>
<meta charset="utf-8">
<title>Eyelid Specialists of the Brenwick — Business Card</title>
<link href="https://fonts.googleapis.com/css2?family=Open+Sans:wght@300;400&display=swap" rel="stylesheet">
<style>
  :root {
    --page-bg: #e9e7e3;
    --card-white: #ffffff;
    --brand-blue: #1f5fb8;
    --swoosh-deep: #3a55b8;
    --swoosh-light: #4e9ad8;
    --arc-grey: #d4d6da;
    --text-grey: #6b6b6b;
    --text-soft: #8a8a8a;
  }
  html, body {
    margin: 0;
    width: 1200px;
    height: 900px;
    overflow: hidden;
    background: var(--page-bg);
    font-family: "Open Sans", Arial, sans-serif;
  }
  .business-card {
    position: absolute;
    left: 100px;
    top: 164px;
    width: 1000px;
    height: 572px;
    background: var(--card-white);
    box-shadow: 0 10px 30px rgba(0,0,0,0.18);
    overflow: hidden;
  }
  .card-swoosh {
    position: absolute;
    inset: 0;
    width: 100%;
    height: 100%;
  }
  .brand-name {
    position: absolute;
    right: 70px;
    top: 64px;
    margin: 0;
    color: var(--brand-blue);
    font-size: 30px;
    font-weight: 400;
    line-height: 1;
    white-space: nowrap;
  }
  .person {
    position: absolute;
    left: 190px;
    top: 318px;
    color: var(--text-grey);
  }
  .person-name {
    margin: 0;
    font-size: 60px;
    font-weight: 400;
    line-height: 1;
  }
  .person-role {
    margin: 6px 0 0 130px;
    font-size: 18px;
    font-weight: 400;
  }
  .contact-list {
    position: absolute;
    left: 500px;
    top: 228px;
    margin: 0;
    padding: 0;
    list-style: none;
    color: var(--text-soft);
    font-size: 24px;
    font-weight: 300;
    line-height: 1.1;
  }
  .contact-list li:nth-child(2) { padding-left: 10px; }
  .contact-list li:nth-child(3) { padding-left: 20px; }
</style>
</head>
<body>
  <div class="business-card">
    <svg class="card-swoosh" viewBox="0 0 1000 572" preserveAspectRatio="none" aria-hidden="true">
      <defs>
        <linearGradient id="swooshGradient" x1="0" y1="0" x2="1" y2="1">
          <stop offset="0" stop-color="var(--swoosh-deep)"/>
          <stop offset="0.45" stop-color="var(--swoosh-light)"/>
          <stop offset="1" stop-color="var(--swoosh-deep)"/>
        </linearGradient>
      </defs>
      <rect width="1000" height="572" fill="url(#swooshGradient)"/>
      <ellipse cx="500" cy="296" rx="640" ry="250" transform="rotate(-14 500 296)"
               fill="var(--card-white)" stroke="var(--arc-grey)" stroke-width="14"/>
      <ellipse cx="500" cy="296" rx="612" ry="228" transform="rotate(-14 500 296)"
               fill="none" stroke="var(--card-white)" stroke-width="6"/>
    </svg>

    <p class="brand-name">Eyelid Specialists of the Brenwick</p>

    <ul class="contact-list">
      <li>address</li>
      <li>phone number</li>
      <li>email address</li>
    </ul>

    <div class="person">
      <h1 class="person-name">John Doe</h1>
      <p class="person-role">Position</p>
    </div>
  </div>
</body>
</html>
```